Clerodent distributor needs basic website

We need a website for a Philippines distribution company of Clerodent. The purpose is to redirect the user to the corporate site if they need more information, and to provide the user a list of available doctors in the Philippines. I've attached a word document with a rough outline of the content. Below is a description of the pages needed.
• Home page: Use Clerodent logo on the top and provide a nicer graphical representation of the text. For example, "Philippines" is plain but I would like to look a little nicer graphically, maybe tying in the Clerodent graphic.
• What is Clerodent? This link should open a new tab, keeping the original home page open. Can you make this text graphically nicer?
• Find an Clerodent Doctor (info on page 2-3 of the attachment): Is there a cool way to show the list of doctors and still keep the user on the home page? There are currently about 15 doctors and the list may grow to about 30-40. We will need the ability to change the doctor list content. Can you also make this text graphically nicer?
* Create a category called "Sign Me Up"? It should then allow open a subwindow within this page to open and have the user fill out a form. The form should have a pull down for Dentist or Patient. That way when we receive it, we know how to handle it.
• Create basic company logo for Paskor Distribution, Inc (the distribution company) and put on bottom. Logo needs to be available to work on letterhead and the future website design.
I'm okay if you want to add Flash elements to make it more interesting, but it should be designed as a site for high end consumers.
Thank you,
Wes
Target Market(s)
The product sells for $5000 per transaction so the site should reflect this target market.
Industry/Entity Type
Doctor
Look and feel
Each slider illustrates characteristics of the customer's brand and the style your logo design should communicate.

```html
<!DOCTYPE html>
<html lang="en">
<head>
<meta charset="utf-8">
<title>Clerodent Philippines</title>
<link href="https://fonts.googleapis.com/css2?family=Raleway:wght@300;400;600&family=Varela+Round&display=swap" rel="stylesheet">
<style>
:root{
  --teal:#4fa6bb;
  --teal-dark:#3b8fa4;
  --teal-light:#5bb6cc;
  --orange:#ef5a24;
  --orange-soft:#f47a45;
  --text:#555;
  --muted:#999;
  --line:#e4e4e4;
  --panel:#e9e9e9;
  --dark:#2e3335;
  --darker:#252a2b;
  --blue:#1f7fc4;
}
*{box-sizing:border-box;margin:0;padding:0}
html,body{width:960px;height:1200px;overflow:hidden;background:#fff}
body{position:relative;font-family:"Varela Round",sans-serif;color:var(--text)}
.abs{position:absolute}
.brand{left:164px;top:27px}
.brand-name{font-size:16px;color:var(--blue);display:flex;align-items:center;gap:6px}
.brand-mark{width:12px;height:12px;border-radius:50%;background:var(--blue)}
.brand-sub{font-size:8px;color:var(--blue);margin-left:39px;margin-top:1px}
.social{left:438px;top:14px;display:flex;gap:6px}
.pill{height:18px;width:28px;border:1px solid #ddd;border-radius:9px;display:flex;align-items:center;justify-content:center}
.pill span{width:6px;height:6px;border-radius:50%;background:#ccc}
.pill.phone{width:103px;font-size:7px;color:#bbb;gap:5px}
.nav{left:142px;top:67px;width:629px;height:17px;background:var(--teal);display:flex;align-items:center;font-size:7px;color:#e3f3f7}
.nav a{padding:0 12px;border-right:1px solid rgba(255,255,255,.25);line-height:17px;text-decoration:none;color:inherit}
.search{position:absolute;right:5px;top:3px;width:132px;height:11px;background:var(--teal-dark);font-size:6px;color:#9fd0dc;padding-left:7px;line-height:11px}
.search svg{position:absolute;right:4px;top:2px}
.hero{left:142px;top:84px;width:629px;height:196px;background:linear-gradient(135deg,#dfe8ef 0%,#c9d6e0 45%,#e8ecee 70%,#d2dde4 100%)}
.tabs{left:142px;top:280px;width:629px;height:34px;display:flex;background:var(--orange)}
.tab{flex:1;padding:8px 12px;border-right:1px solid rgba(255,255,255,.3);color:#fff}
.tab b{display:block;font-size:7px;font-weight:600;font-family:"Raleway",sans-serif}
.tab small{display:block;font-size:6px;color:#fdd;margin-top:3px}
.tab.active{background:#e04b16}
.headline{left:0;width:913px;top:332px;text-align:center;font-family:"Raleway",sans-serif;font-weight:300;font-size:15.5px;color:var(--teal-light);letter-spacing:.5px}
.subline{left:0;width:913px;top:353px;text-align:center;font-size:8.5px;color:var(--teal)}
.service{top:378px;width:120px;text-align:center}
.ring{width:72px;height:50px;margin:0 auto;border:1.5px solid #ccc;border-radius:50%;display:flex;align-items:center;justify-content:center}
.service h3{font-family:"Raleway",sans-serif;font-weight:600;font-size:8.5px;color:#444;margin-top:10px}
.service p{font-size:6.3px;color:var(--orange-soft);line-height:9.2px;margin-top:5px;padding:0 6px}
.rule{left:142px;top:531px;width:629px;height:1px;background:var(--line)}
.section-title{font-family:"Raleway",sans-serif;font-weight:300;font-size:15px;color:var(--teal-light);letter-spacing:.4px}
.section-sub{font-size:6.3px;color:var(--muted);margin-top:3px}
.doctor{top:604px;width:124px}
.photo{height:66px;border:2px solid #e6e6e6;position:relative;background:linear-gradient(180deg,#e9eef0,#d5dde0)}
.tag{position:absolute;right:0;bottom:0;background:#6a6a6a;color:#eee;font-size:6px;padding:2px 8px}
.doctor p{font-size:6.3px;color:var(--orange-soft);line-height:9.2px;margin-top:13px}
.btn{background:var(--orange);color:#fff;font-size:6.5px;display:inline-block;padding:3px 10px;border-radius:1px}
.avatar{left:147px;top:812px;width:44px;height:34px;border-radius:50%;border:2px solid #ddd;background:linear-gradient(180deg,#e7d9c8,#a9bf8f)}
.quote{left:207px;top:814px;width:335px;font-style:italic;font-size:7.8px;line-height:10.4px;color:#888}
.author{left:142px;top:873px;font-size:6.5px;color:var(--orange-soft)}
.author span{color:#888}
.arrows{left:206px;top:892px;display:flex;gap:3px}
.arrows span{width:11px;height:7px;background:#ddd;border-radius:2px}
.signup{left:574px;top:558px;width:197px;height:256px;background:var(--panel)}
.signup-head{height:48px;background:var(--teal);color:#fff;padding:7px 15px;font-family:"Raleway",sans-serif}
.signup-head .t{font-size:12px;letter-spacing:.6px}
.signup-head .ph{font-size:12px;margin-top:4px;display:flex;align-items:center;gap:10px;letter-spacing:.8px}
.ph i{width:18px;height:11px;border-radius:6px;background:var(--teal-dark);display:inline-block}
.or{position:absolute;left:88px;top:42px;width:22px;height:12px;border-radius:6px;background:var(--orange);color:#fff;font-size:6px;text-align:center;line-height:12px}
.field{position:absolute;left:20px;width:158px;height:14px;background:#fff;border:1px solid #ddd;font-size:6px;color:#bbb;padding-left:6px;line-height:12px}
.field.select{color:#888}
.field.select svg{position:absolute;right:5px;top:4px}
.captcha{position:absolute;left:22px;top:206px;width:52px;height:14px;background:#fff;font-size:9px;color:#c0392b;padding-left:6px;letter-spacing:1px;line-height:14px;font-family:"Raleway",sans-serif}
.captcha-in{position:absolute;left:80px;top:206px;width:42px;height:14px;background:#fff;border:1px solid #ddd}
.news-title{left:574px;top:834px}
.news{left:574px;top:854px;width:197px;height:50px;background:var(--panel);padding:9px 13px;font-size:6px;color:#999}
.news .row{display:flex;gap:8px;margin-top:7px}
.news .in{width:106px;height:14px;background:#fff;border:1px solid #ddd;font-size:6px;line-height:12px;padding-left:6px;color:#bbb}
.tweet{left:142px;top:970px;width:629px;height:28px;background:var(--teal);color:#eaf6f9;font-size:6.5px;display:flex;align-items:center;padding-left:14px;gap:25px}
.tweet i{width:22px;height:14px;border-radius:50%;background:var(--teal-dark);display:inline-block}
.footer{left:134px;top:998px;width:646px;height:202px;background:var(--dark)}
.copy{position:absolute;left:0;bottom:0;width:100%;height:22px;background:var(--darker);font-size:6.3px;color:#6d7476;padding:7px 9px}
.fcol{position:absolute;top:31px;width:150px}
.fcol h4{font-family:"Raleway",sans-serif;font-weight:400;font-size:12px;color:#ccd;letter-spacing:.5px}
.company{display:flex;align-items:center;gap:6px;font-family:"Raleway",sans-serif;font-weight:600;font-size:11px;color:#fff;letter-spacing:.3px}
.company i{width:10px;height:10px;background:var(--orange);display:inline-block}
.fcol p,.fcol li{font-size:6.3px;color:#7d8587;line-height:9.2px}
.fcol ul{list-style:none;margin-top:13px}
.fcol li::before{content:"- ";color:#999}
.fcol li{color:#b8bfc1;line-height:11px}
.fcol .light{color:#c5cbcd}
</style>
</head>
<body>

<header>
  <div class="abs brand">
    <div class="brand-name"><span class="brand-mark"></span>Clerodent</div>
    <div class="brand-sub">Philippines</div>
  </div>
  <div class="abs social">
    <div class="pill"><span></span></div>
    <div class="pill"><span></span></div>
    <div class="pill"><span></span></div>
    <div class="pill"><span></span></div>
    <div class="pill"><span></span></div>
    <div class="pill"><span></span></div>
    <div class="pill"><span></span></div>
    <div class="pill phone">
      <svg width="8" height="8" viewBox="0 0 8 8"><rect x="1" y="1" width="6" height="6" rx="1" fill="none" stroke="#bbb"/><rect x="2.5" y="2.5" width="3" height="1.5" fill="#bbb"/></svg>
      1.800.555.0142
    </div>
  </div>
  <nav class="abs nav">
    <a>What is Clerodent</a>
    <a>Find a Clerodent Doctor</a>
    <a>Sign Me Up</a>
    <a>Disclaimer</a>
    <a style="border:none">Contact Us</a>
    <div class="search">Search
      <svg width="8" height="8" viewBox="0 0 8 8"><circle cx="3.3" cy="3.3" r="2.4" fill="none" stroke="#fff" stroke-width="1"/><line x1="5" y1="5" x2="7.5" y2="7.5" stroke="#fff" stroke-width="1.2"/></svg>
    </div>
  </nav>
</header>

<div class="abs hero" role="img" aria-label="Photo of two clinicians in lab coats and goggles examining a test tube in a bright laboratory"></div>

<div class="abs tabs">
  <div class="tab"><b>Certified Doctors</b><small>Nationwide Clinic Network</small></div>
  <div class="tab"><b>Clinical Excellence</b><small>Precise Aligner Planning</small></div>
  <div class="tab active"><b>Clear Aligners</b><small>Discreet Dental Treatment</small></div>
  <div class="tab"><b>Caring Staff</b><small>Personal Guidance</small></div>
  <div class="tab" style="border:none"><b>Consultation</b><small>Discuss Your Smile</small></div>
</div>

<h1 class="abs headline">Confident Smiles, Crafted by Certified Clerodent Doctors</h1>
<p class="abs subline">Premium clear aligner care, available across the Philippines</p>

<section>
  <div class="abs service" style="left:146px">
    <div class="ring"><svg width="22" height="18" viewBox="0 0 22 18"><rect x="1" y="4" width="20" height="13" rx="2" fill="#ccc"/><rect x="4" y="7" width="11" height="7" fill="#fff"/><line x1="7" y1="0" x2="11" y2="4" stroke="#ccc" stroke-width="1.5"/><line x1="15" y1="0" x2="11" y2="4" stroke="#ccc" stroke-width="1.5"/></svg></div>
    <h3>Digital Scanning</h3>
    <p>A quick, comfortable 3D scan replaces messy impressions and maps your teeth with precision for a plan built around you.</p>
  </div>
  <div class="abs service" style="left:271px">
    <div class="ring"><svg width="24" height="12" viewBox="0 0 24 12"><path d="M1 6 Q12 -4 23 6 Q12 16 1 6Z" fill="#ccc"/><circle cx="12" cy="6" r="3.5" fill="#fff"/><circle cx="12" cy="6" r="2" fill="#ccc"/></svg></div>
    <h3>Smile Preview</h3>
    <p>See a virtual preview of your new smile before treatment begins, so every step is clear and agreed with your doctor.</p>
  </div>
  <div class="abs service" style="left:397px">
    <div class="ring"><svg width="22" height="18" viewBox="0 0 22 18"><rect x="7" y="1" width="8" height="4" rx="1" fill="none" stroke="#ccc" stroke-width="1.5"/><rect x="1" y="4" width="20" height="13" rx="2" fill="#ccc"/><rect x="9.5" y="6.5" width="3" height="8" fill="#fff"/><rect x="7" y="9" width="8" height="3" fill="#fff"/></svg></div>
    <h3>Custom Aligners</h3>
    <p>Each set of clear aligners is made for your teeth alone, nearly invisible and removable for meals and daily brushing.</p>
  </div>
  <div class="abs service" style="left:522px">
    <div class="ring"><svg width="20" height="20" viewBox="0 0 20 20"><path d="M3 2 L7 2 L8 6 L6 8 Q9 12 12 14 L14 12 L18 13 L18 17 Q10 19 5 12 Q1 6 3 2Z" fill="#ccc"/></svg></div>
    <h3>Doctor Locator</h3>
    <p>Find a certified Clerodent doctor near you in Metro Manila, Cebu, Davao and other cities across the Philippines.</p>
  </div>
  <div class="abs service" style="left:649px">
    <div class="ring"><svg width="14" height="20" viewBox="0 0 14 20"><path d="M7 1 Q13 10 13 13 A6 6 0 0 1 1 13 Q1 10 7 1Z" fill="#ccc"/></svg></div>
    <h3>Lasting Aftercare</h3>
    <p>Retainers and regular check-ins with your doctor keep results in place long after your final aligner is finished.</p>
  </div>
</section>

<div class="abs rule"></div>

<section>
  <div class="abs" style="left:142px;top:559px">
    <h2 class="section-title">Find a Clerodent Doctor</h2>
    <p class="section-sub">Browse certified providers across the Philippines.</p>
  </div>
  <div class="abs doctor" style="left:142px">
    <div class="photo" role="img" aria-label="Portrait photo of a smiling female dentist"><span class="tag">Makati</span></div>
    <p>Dr. Ana Reyes – Makati Dental Studio. Certified Clerodent provider since 2015. Book a consultation...</p>
  </div>
  <div class="abs doctor" style="left:286px">
    <div class="photo" role="img" aria-label="Portrait photo of a female dentist"><span class="tag">Cebu</span></div>
    <p>Dr. Carla Lim – Cebu Smile Clinic. Certified Clerodent provider since 2017. Book a consultation...</p>
  </div>
  <div class="abs doctor" style="left:430px">
    <div class="photo" role="img" aria-label="Portrait photo of a male dentist with a stethoscope"><span class="tag">Davao</span></div>
    <p>Dr. Ramon Cruz – Davao Orthodontic Center. Certified Clerodent provider since 2016. Book a consultation...</p>
  </div>
  <div class="abs btn" style="left:142px;top:729px">View All Doctors</div>
</section>

<section>
  <div class="abs" style="left:142px;top:769px">
    <h2 class="section-title">What our patients say</h2>
    <p class="section-sub">Real stories from Clerodent patients in the Philippines.</p>
  </div>
  <div class="abs avatar" role="img" aria-label="Small portrait photo of a smiling older patient"></div>
  <p class="abs quote">I put off straightening my teeth for years because I did not want metal braces at work. With Clerodent, nobody noticed I was in treatment. My doctor guided me at every visit, and the whole process felt calm and personal. Today I smile in every photo and I recommend it to friends.</p>
  <p class="abs author">Miguel Santos, <span>Patient, Quezon City</span></p>
  <div class="abs arrows"><span></span><span></span></div>
</section>

<aside class="abs signup">
  <div class="signup-head">
    <div class="t">Sign Me Up</div>
    <div class="ph"><i></i>1-800-555-0142</div>
  </div>
  <div class="or">OR</div>
  <div class="field" style="top:62px">Full Name</div>
  <div class="field" style="top:84px">Phone Number</div>
  <div class="field" style="top:105px">Email Address</div>
  <div class="field select" style="top:127px">I am a: Dentist / Patient
    <svg width="6" height="4" viewBox="0 0 6 4"><path d="M0 0 L6 0 L3 4Z" fill="#999"/></svg>
  </div>
  <div class="field" style="top:148px;height:49px">Message</div>
  <div class="captcha">bxxoq</div>
  <div class="captcha-in"></div>
  <div class="btn" style="position:absolute;left:20px;top:230px;padding:3px 12px">Submit Request</div>
</aside>

<h2 class="abs section-title news-title">Newsletter</h2>
<div class="abs news">
  Sign up for our newsletter to get latest updates
  <div class="row"><div class="in">Email Address</div><div class="btn" style="padding:3px 13px">Go</div></div>
</div>

<div class="abs tweet"><i></i>No Tweet Loaded !</div>

<footer class="abs footer">
  <div class="fcol" style="left:8px">
    <div class="company"><i></i>Paskor Distribution, Inc</div>
    <p style="margin-top:13px">Paskor Distribution, Inc is the authorized distributor of Clerodent clear aligners in the Philippines, serving dentists and patients nationwide.</p>
    <div class="btn" style="margin-top:8px">Read more</div>
  </div>
  <div class="fcol" style="left:171px">
    <h4>Quick Links</h4>
    <ul><li>Home</li><li>What is Clerodent</li><li>Find a Doctor</li><li>Sign Me Up</li><li>Contact Us</li></ul>
  </div>
  <div class="fcol" style="left:332px;width:145px">
    <h4>Recent Posts</h4>
    <ul><li>Clear Aligners vs. Braces</li><li>Caring for Your Aligners Daily</li><li>What to Expect at Your First Consultation Visit</li><li>How Long Does Aligner Treatment Take?</li><li>New Certified Doctors Join Our Network</li></ul>
  </div>
  <div class="fcol" style="left:494px">
    <h4>Location</h4>
    <p style="margin-top:13px">Unit 12, Ayala Business Park, Makati City, Metro Manila, Philippines.</p>
    <p class="light" style="margin-top:9px">Ph: +800 555 0142</p>
    <p class="light" style="margin-top:9px">Email: hello@paskor-ph.example</p>
  </div>
  <div class="copy">© Copyright 2012. All Rights Reserved by Paskor Distribution, Inc.</div>
</footer>

</body>
</html>
```